Packaged Food Business Needs a Packaging Design

We need a package design to be used as a label/sticker on the lids of round and square transparent plastic containers and on the sides of resealable stand-up pouches. The brand name is 'Tastora' - please find attached logo together with pictures of the sample containers and pouch. We will use the packaging to market a wide variety of food categories from nuts, dried fruits, spices, cooking chocolates, baking ingredients, cereals, grains and pulses.

OVERALL FEEDBACK ON DESIGNS ALREADY RECEIVED:

- We have found so far that a lot of our mandatory requirements are not adhered to in designs that have been submitted so far. We would like to emphasise that the ingredient, weight and expiry text will be printed at the time of packing so it should not take prime space on the pack BUT at the same time some 'blank' space needs to flawlessly be incorporated into the overall design for this purpose
- We encourage you to glorify the brand logo in the pack, and absolutely refrain from duplicating the tagline
- Please note that ONE label design will be used to pack a wide variety of food ingredients and therefore please ensure that the choice of your design incorporates this requirement, in the past we have received designs that are limited to only one type of food (like nuts) or have received designs that are too floral or leafy (and not grounded to food
- Please ensure that you submit designs for all three packaging formats, it is critical to see the family look from the on-set

Target Market(s)

The brand is targeting both mothers and professional chefs and therefore the label design should be broadly approachable and convey affordable premium

Industry/Entity Type

Business

Requirements
Must have
• - Consistent with the brand name and logo, the overall look and feel of the packaging should convey values of healthy, gourmet food ingredients, high in nourishment and project a sense of delightful taste
• - The design styling to be modern and 'simplistic' (embracing 'less-is-more' type of a design style)
• - Design a packaging architecture that incorporates the brand logo together with its tagline lock-up of 'savour the goodness in every morsel' - find logo attached
• - The design needs to have a dedicated area to print the ingredient (e.g., Mixed Nuts), weight (e.g., 500g) and expiry (this space needs to be flawlessly incorporated into the design) - this information will be printed either with an inkjet printer or with a rubber stamp so please leave an empty space (the text should not be part of the design, just the area for the text needs to be included in the design)
• - The packaging must include 'Packed By: Kelvane Distributors Ltd, P. O. Box 51946, Kampala - Uganda'
• - For the design of the resealable pouch, please incorporate a window to see through the ingredients and a hole on top to hang on supermarket pegs if necessary
Nice to have
• - We would love to have some design submissions that are bold and cheerful and fun (but not frivolous) - please see attached inspiration for 'fun' packaging. The attachments are purely for inspiration, not to infringe on anyone else's TM and copyrights
• - Incorporate green to convey healthy, organic values
• - Explore use of gold and silver convey premiumness
Should not have
• - Do not duplicate the tagline
• - Do not include the ingredient, weight and expiry in the main graphic of the design, these will be printed at the time of packing so ensure there is provision for this in a flawless way in the design (e.g., via a blank space allocated for this purpose)

```html
<!DOCTYPE html>
<html lang="en">
<head>
<meta charset="utf-8">
<title>Tastora Label and Pouch Family</title>
<link rel="stylesheet" href="https://fonts.googleapis.com/css2?family=Oswald:wght@500;600&family=Archivo:wght@700;800&display=swap">
<style>
  :root {
    --canvas: #ffffff;
    --band: #1c1c1c;
    --white: #ffffff;
    --brand-brown: #2b1a10;
    --green: #7ed321;
    --green-dark: #4e9a12;
    --orange: #f7901e;
    --red: #e5333b;
    --chocolate: #4a2a17;
    --cyan: #52d9f2;
    --film: #dfe2e5;
    --seam: #b9bec3;
  }
  html, body {
    margin: 0;
    padding: 0;
    width: 1200px;
    height: 1200px;
    overflow: hidden;
    background: var(--canvas);
  }
  .canvas { position: relative; width: 1200px; height: 1200px; }
  .defs { position: absolute; width: 0; height: 0; }
  .range-band {
    position: absolute;
    left: 0; top: 858px;
    width: 1200px; height: 342px;
    background: var(--band);
  }
  .label, .pouch { position: absolute; display: block; }
  .label--master { left: 60px; top: 42px; width: 518px; height: 752px; }
  .pouch--feature { left: 674px; top: 44px; width: 464px; height: 748px; }
  .pouch--range { top: 886px; width: 176px; height: 284px; }
  .pouch--cereals { left: 33px; }
  .pouch--spices { left: 270px; }
  .pouch--chocolate { left: 506px; }
  .pouch--fruits { left: 743px; }
  .pouch--grains { left: 980px; }

  .brand-name {
    font-family: "Oswald", sans-serif;
    font-weight: 600;
    fill: var(--brand-brown);
  }
  .tagline {
    font-family: "Archivo", sans-serif;
    font-weight: 800;
    fill: var(--green-dark);
  }
  .category {
    font-family: "Oswald", sans-serif;
    font-weight: 600;
  }
  .packed-by {
    font-family: "Archivo", sans-serif;
    font-weight: 700;
    fill: var(--white);
  }
  .print-area, .logo-oval { fill: var(--white); }
  .pouch-film { fill: url(#film-sheen); }
  .zip-seal { stroke: var(--seam); stroke-width: 3; }
  .hang-hole { fill: var(--canvas); stroke: var(--seam); stroke-width: 2; }
  .pouch--range .hang-hole { fill: var(--band); }
  .product-window { fill: url(#window-contents); }

  .theme--green .label-body { fill: var(--green); }
  .theme--green .category { fill: var(--green); }
  .theme--orange .label-body { fill: var(--orange); }
  .theme--orange .category { fill: var(--orange); }
  .theme--red .label-body { fill: var(--red); }
  .theme--red .category { fill: var(--red); }
  .theme--chocolate .label-body { fill: var(--chocolate); }
  .theme--chocolate .category { fill: var(--brand-brown); }
  .theme--cyan .label-body { fill: var(--cyan); }
  .theme--cyan .category { fill: var(--cyan); }
</style>
</head>
<body>
<main class="canvas">

  <svg class="defs" aria-hidden="true">
    <defs>
      <linearGradient id="film-sheen" x1="0" y1="0" x2="1" y2="0">
        <stop offset="0" stop-color="#c9cdd1"/>
        <stop offset="0.45" stop-color="#f1f2f4"/>
        <stop offset="1" stop-color="#cfd3d7"/>
      </linearGradient>
      <linearGradient id="window-contents" x1="0" y1="0" x2="1" y2="0">
        <stop offset="0" stop-color="#e9e4dc"/>
        <stop offset="0.25" stop-color="#8a5a34"/>
        <stop offset="0.55" stop-color="#c9a57a"/>
        <stop offset="0.8" stop-color="#6b4a30"/>
        <stop offset="1" stop-color="#efeae3"/>
      </linearGradient>
    </defs>
  </svg>

  <!-- Flat sticker for lids and containers -->
  <svg class="label label--master theme--green" viewBox="0 0 648 942" aria-label="Tastora container label">
    <g role="img" aria-label="Green label background with a light food-and-leaf pattern">
      <rect class="label-body" x="0" y="0" width="648" height="942" rx="22"/>
    </g>
    <rect class="print-area" x="48" y="43" width="570" height="133" rx="30"/>
    <ellipse class="logo-oval" cx="322" cy="438" rx="250" ry="184"/>
    <text class="brand-name" x="322" y="482" text-anchor="middle" font-size="92" textLength="470" lengthAdjust="spacingAndGlyphs">TASTORA</text>
    <text class="tagline" x="322" y="508" text-anchor="middle" font-size="15" textLength="458" lengthAdjust="spacingAndGlyphs">SAVOUR THE GOODNESS IN EVERY MORSEL!</text>
    <rect class="print-area" x="48" y="706" width="570" height="133" rx="30"/>
    <text class="packed-by" x="333" y="922" text-anchor="middle" font-size="19" textLength="585" lengthAdjust="spacingAndGlyphs">Packed By: Kelvane Distributors Ltd, P. O. Box 51946, Kampala - Uganda</text>
  </svg>

  <!-- Stand-up pouch, featured -->
  <svg class="pouch pouch--feature theme--green" viewBox="0 0 464 748" aria-label="Grains and pulses stand-up pouch">
    <rect class="pouch-film" x="0" y="0" width="464" height="748" rx="16"/>
    <circle class="hang-hole" cx="232" cy="30" r="10"/>
    <line class="zip-seal" x1="14" y1="72" x2="450" y2="72"/>
    <g role="img" aria-label="Green label background with a light food pattern">
      <rect class="label-body" x="20" y="108" width="424" height="624" rx="16"/>
    </g>
    <rect class="print-area" x="48" y="140" width="368" height="92" rx="18"/>
    <text class="category" x="232" y="204" text-anchor="middle" font-size="44" textLength="324" lengthAdjust="spacingAndGlyphs">GRAINS &amp; PULSES</text>
    <ellipse class="logo-oval" cx="232" cy="404" rx="156" ry="118"/>
    <text class="brand-name" x="232" y="432" text-anchor="middle" font-size="60" textLength="236" lengthAdjust="spacingAndGlyphs">TASTORA</text>
    <text class="tagline" x="232" y="448" text-anchor="middle" font-size="10" textLength="228" lengthAdjust="spacingAndGlyphs">SAVOUR THE GOODNESS IN EVERY MORSEL!</text>
    <rect class="product-window" x="60" y="572" width="346" height="82" rx="16" role="img" aria-label="Clear window showing the grains and pulses inside"/>
    <text class="packed-by" x="232" y="712" text-anchor="middle" font-size="10" textLength="330" lengthAdjust="spacingAndGlyphs">Packed By: Kelvane Distributors Ltd, P. O. Box 51946, Kampala - Uganda</text>
  </svg>

  <div class="range-band" aria-hidden="true"></div>

  <!-- Pouch range -->
  <svg class="pouch pouch--range pouch--cereals theme--orange" viewBox="0 0 464 748" aria-label="Cereals pouch">
    <rect class="pouch-film" x="0" y="0" width="464" height="748" rx="16"/>
    <circle class="hang-hole" cx="232" cy="30" r="10"/>
    <line class="zip-seal" x1="14" y1="72" x2="450" y2="72"/>
    <g role="img" aria-label="Orange label background with a light food pattern"><rect class="label-body" x="20" y="108" width="424" height="624" rx="16"/></g>
    <rect class="print-area" x="48" y="140" width="368" height="92" rx="18"/>
    <text class="category" x="232" y="206" text-anchor="middle" font-size="48" textLength="190" lengthAdjust="spacingAndGlyphs">CEREALS</text>
    <ellipse class="logo-oval" cx="232" cy="404" rx="156" ry="118"/>
    <text class="brand-name" x="232" y="432" text-anchor="middle" font-size="60" textLength="236" lengthAdjust="spacingAndGlyphs">TASTORA</text>
    <text class="tagline" x="232" y="448" text-anchor="middle" font-size="10" textLength="228" lengthAdjust="spacingAndGlyphs">SAVOUR THE GOODNESS IN EVERY MORSEL!</text>
    <rect class="product-window" x="60" y="572" width="346" height="82" rx="16" role="img" aria-label="Clear window showing the cereals inside"/>
    <text class="packed-by" x="232" y="712" text-anchor="middle" font-size="10" textLength="330" lengthAdjust="spacingAndGlyphs">Packed By: Kelvane Distributors Ltd, P. O. Box 51946, Kampala - Uganda</text>
  </svg>

  <svg class="pouch pouch--range pouch--spices theme--red" viewBox="0 0 464 748" aria-label="Spices pouch">
    <rect class="pouch-film" x="0" y="0" width="464" height="748" rx="16"/>
    <circle class="hang-hole" cx="232" cy="30" r="10"/>
    <line class="zip-seal" x1="14" y1="72" x2="450" y2="72"/>
    <g role="img" aria-label="Red label background with a light food pattern"><rect class="label-body" x="20" y="108" width="424" height="624" rx="16"/></g>
    <rect class="print-area" x="48" y="140" width="368" height="92" rx="18"/>
    <text class="category" x="232" y="206" text-anchor="middle" font-size="48" textLength="170" lengthAdjust="spacingAndGlyphs">SPICES</text>
    <ellipse class="logo-oval" cx="232" cy="404" rx="156" ry="118"/>
    <text class="brand-name" x="232" y="432" text-anchor="middle" font-size="60" textLength="236" lengthAdjust="spacingAndGlyphs">TASTORA</text>
    <text class="tagline" x="232" y="448" text-anchor="middle" font-size="10" textLength="228" lengthAdjust="spacingAndGlyphs">SAVOUR THE GOODNESS IN EVERY MORSEL!</text>
    <rect class="product-window" x="60" y="572" width="346" height="82" rx="16" role="img" aria-label="Clear window showing the spices inside"/>
    <text class="packed-by" x="232" y="712" text-anchor="middle" font-size="10" textLength="330" lengthAdjust="spacingAndGlyphs">Packed By: Kelvane Distributors Ltd, P. O. Box 51946, Kampala - Uganda</text>
  </svg>

  <svg class="pouch pouch--range pouch--chocolate theme--chocolate" viewBox="0 0 464 748" aria-label="Chocolate pouch">
    <rect class="pouch-film" x="0" y="0" width="464" height="748" rx="16"/>
    <circle class="hang-hole" cx="232" cy="30" r="10"/>
    <line class="zip-seal" x1="14" y1="72" x2="450" y2="72"/>
    <g role="img" aria-label="Chocolate brown label background with a light food pattern"><rect class="label-body" x="20" y="108" width="424" height="624" rx="16"/></g>
    <rect class="print-area" x="48" y="140" width="368" height="92" rx="18"/>
    <text class="category" x="232" y="206" text-anchor="middle" font-size="48" textLength="262" lengthAdjust="spacingAndGlyphs">CHOCOLATE</text>
    <ellipse class="logo-oval" cx="232" cy="404" rx="156" ry="118"/>
    <text class="brand-name" x="232" y="432" text-anchor="middle" font-size="60" textLength="236" lengthAdjust="spacingAndGlyphs">TASTORA</text>
    <text class="tagline" x="232" y="448" text-anchor="middle" font-size="10" textLength="228" lengthAdjust="spacingAndGlyphs">SAVOUR THE GOODNESS IN EVERY MORSEL!</text>
    <rect class="product-window" x="60" y="572" width="346" height="82" rx="16" role="img" aria-label="Clear window showing the chocolate inside"/>
    <text class="packed-by" x="232" y="712" text-anchor="middle" font-size="10" textLength="330" lengthAdjust="spacingAndGlyphs">Packed By: Kelvane Distributors Ltd, P. O. Box 51946, Kampala - Uganda</text>
  </svg>

  <svg class="pouch pouch--range pouch--fruits theme--cyan" viewBox="0 0 464 748" aria-label="Dried fruits pouch">
    <rect class="pouch-film" x="0" y="0" width="464" height="748" rx="16"/>
    <circle class="hang-hole" cx="232" cy="30" r="10"/>
    <line class="zip-seal" x1="14" y1="72" x2="450" y2="72"/>
    <g role="img" aria-label="Light blue label background with a light food pattern"><rect class="label-body" x="20" y="108" width="424" height="624" rx="16"/></g>
    <rect class="print-area" x="48" y="140" width="368" height="92" rx="18"/>
    <text class="category" x="232" y="206" text-anchor="middle" font-size="48" textLength="318" lengthAdjust="spacingAndGlyphs">DRIED FRUITS</text>
    <ellipse class="logo-oval" cx="232" cy="404" rx="156" ry="118"/>
    <text class="brand-name" x="232" y="432" text-anchor="middle" font-size="60" textLength="236" lengthAdjust="spacingAndGlyphs">TASTORA</text>
    <text class="tagline" x="232" y="448" text-anchor="middle" font-size="10" textLength="228" lengthAdjust="spacingAndGlyphs">SAVOUR THE GOODNESS IN EVERY MORSEL!</text>
    <rect class="product-window" x="60" y="572" width="346" height="82" rx="16" role="img" aria-label="Clear window showing the dried fruits inside"/>
    <text class="packed-by" x="232" y="712" text-anchor="middle" font-size="10" textLength="330" lengthAdjust="spacingAndGlyphs">Packed By: Kelvane Distributors Ltd, P. O. Box 51946, Kampala - Uganda</text>
  </svg>

  <svg class="pouch pouch--range pouch--grains theme--green" viewBox="0 0 464 748" aria-label="Grains and pulses pouch">
    <rect class="pouch-film" x="0" y="0" width="464" height="748" rx="16"/>
    <circle class="hang-hole" cx="232" cy="30" r="10"/>
    <line class="zip-seal" x1="14" y1="72" x2="450" y2="72"/>
    <g role="img" aria-label="Green label background with a light food pattern"><rect class="label-body" x="20" y="108" width="424" height="624" rx="16"/></g>
    <rect class="print-area" x="48" y="140" width="368" height="92" rx="18"/>
    <text class="category" x="232" y="206" text-anchor="middle" font-size="48" textLength="330" lengthAdjust="spacingAndGlyphs">GRAINS &amp; PULSES</text>
    <ellipse class="logo-oval" cx="232" cy="404" rx="156" ry="118"/>
    <text class="brand-name" x="232" y="432" text-anchor="middle" font-size="60" textLength="236" lengthAdjust="spacingAndGlyphs">TASTORA</text>
    <text class="tagline" x="232" y="448" text-anchor="middle" font-size="10" textLength="228" lengthAdjust="spacingAndGlyphs">SAVOUR THE GOODNESS IN EVERY MORSEL!</text>
    <rect class="product-window" x="60" y="572" width="346" height="82" rx="16" role="img" aria-label="Clear window showing the grains and pulses inside"/>
    <text class="packed-by" x="232" y="712" text-anchor="middle" font-size="10" textLength="330" lengthAdjust="spacingAndGlyphs">Packed By: Kelvane Distributors Ltd, P. O. Box 51946, Kampala - Uganda</text>
  </svg>

</main>
</body>
</html>
```